Coral Ridge Networks Ltd

I need a website that is an informational only. We are a construction business building telecommunications sites. Seeing how our company is Coral Ridge the color blue might want to be incorporated in the color scheme.
I can provide more picture of towers and wireless communications if needed.
current website www.coralridgenet.ca

Industry/Entity Type

Wireless Telecommunications, Construction

Coding

Coded - Design and coding required

Number of Pages Required

2 page

Font styles to use
Sans Serif

Colors

Designer to choose colors to be used in the design.

```html
<!DOCTYPE html>
<html lang="en">
<head>
<meta charset="utf-8">
<title>Coral Ridge Networks Ltd</title>
<link href="https://fonts.googleapis.com/css2?family=Ubuntu:wght@400;500;700&family=Poppins:wght@400;500;600&display=swap" rel="stylesheet">
<style>
:root{
  --blue:#4a7fc1;
  --blue-dark:#2f5d9e;
  --ink:#1d1d1d;
  --text:#3a3a3a;
  --muted:#8a8a8a;
  --canvas:#f3f3f3;
  --page:#ffffff;
  --panel:#f6f6f6;
  --footer:#2b2b2b;
  --footer-deep:#222222;
  --footer-text:#ffffff;
  --line:#e3e3e3;
}
*{box-sizing:border-box;margin:0;padding:0}
html,body{width:1200px;height:1200px;overflow:hidden}
body{background:var(--canvas);font-family:"Ubuntu",sans-serif;color:var(--text);position:relative}
.page{position:absolute;left:322px;top:0;width:557px;height:1200px;background:var(--page);box-shadow:0 0 28px rgba(0,0,0,.12);overflow:hidden}
.abs{position:absolute}

/* header */
.brand{left:43px;top:8px;font-size:19px;font-weight:500;color:var(--blue);letter-spacing:-.2px;line-height:1}
.nav{right:42px;top:12px;display:flex;align-items:center;gap:10px;font-size:6px;font-weight:700;color:var(--ink);text-transform:uppercase}
.btn{background:var(--blue);color:#fff;border-radius:20px;font-weight:700;text-transform:uppercase;display:flex;align-items:center;justify-content:center;box-shadow:0 2px 5px rgba(0,0,0,.2)}
.nav .btn{width:49px;height:18px;font-size:5.5px;margin-left:4px}

/* hero */
.hero{left:0;top:37px;width:557px;height:225px;background:linear-gradient(90deg,#5e6266 0%,#7b8085 45%,#a7b0b8 75%,#8b8f8c 100%)}
.hero-title{left:43px;top:62px;font-size:18px;font-weight:500;color:#fff;letter-spacing:.3px}
.hero-copy{left:43px;top:88px;width:205px;font-size:5.4px;line-height:11px;color:#f1f1f1}
.checks{left:43px;top:142px;list-style:none;font-size:5.4px;font-weight:700;color:#fff}
.checks li{display:flex;align-items:center;gap:5px;height:14.3px}
.hero-bar{left:182px;top:262px;width:193px;height:3px;background:var(--blue-dark)}

/* about */
.h2{font-size:18px;font-weight:500;color:var(--ink);text-transform:uppercase}
.about-title{left:43px;top:318px}
.about-copy{left:43px;top:343px;width:210px;font-size:5.3px;line-height:11px;text-transform:uppercase;text-align:justify;letter-spacing:.2px}
.about-copy p{margin-bottom:11px}
.about-copy strong{color:var(--blue);font-weight:700}
.call-btn{left:43px;top:469px;width:57px;height:19px;font-size:6px}
.deco{background:var(--blue)}
.deco-top{left:465px;top:294px;width:58px;height:58px}
.deco-bottom{left:281px;top:457px;width:58px;height:59px}
.about-photo{left:290px;top:303px;width:225px;height:204px;border-radius:2px;background:linear-gradient(180deg,#5c6d8a 0%,#b2a58b 45%,#f0b54a 70%,#5a5a3e 100%)}

/* services */
.service-title{left:0;width:557px;top:543px;text-align:center}
.card{top:575px;width:143px;height:179px;background:#fff;box-shadow:0 1px 5px rgba(0,0,0,.12)}
.card.is-active{box-shadow:0 2px 9px rgba(40,80,140,.35);outline:1px solid #c9d7ea}
.card-photo{width:143px;height:115px}
.card h3{font-size:7.8px;font-weight:700;color:var(--ink);margin:6px 6px 3px;text-transform:uppercase}
.card p{font-size:4.3px;line-height:7.6px;margin:0 6px;text-transform:uppercase;text-align:justify;color:#555}
.card .more{position:absolute;right:6px;bottom:7px;font-size:4.5px;font-weight:700;color:var(--blue);text-transform:uppercase;display:flex;align-items:center;gap:2px}

/* contact */
.contact-title{left:0;width:557px;top:779px;text-align:center}
.contact-panel{left:0;top:809px;width:557px;height:256px;background:var(--panel)}
.map{left:0;top:809px;width:259px;height:256px;background:linear-gradient(135deg,#dfe6d6 0%,#e8e8e4 50%,#d9dfe6 100%)}
.map-card{left:40px;top:820px;width:93px;height:32px;background:#fff;box-shadow:0 1px 3px rgba(0,0,0,.25);padding:6px 7px;font-size:6px;color:var(--ink)}
.map-card span{display:block;font-size:5px;color:var(--blue);margin-top:4px}
.map-card i{position:absolute;right:7px;top:9px;width:14px;height:14px;border-radius:50%;background:var(--blue)}
.field{left:273px;width:223px;background:#fff;border:1px solid var(--line);font-size:5.8px;color:var(--muted);padding:7px 8px}
.send-btn{left:274px;top:1027px;width:69px;height:26px;font-size:7px}

/* footer */
.site-footer{color:var(--footer-text)}
.footer{left:0;top:1094px;width:557px;height:106px;background:var(--footer)}
.foot-brand{left:55px;top:1106px;font-size:19px;font-weight:500;color:var(--footer-text);line-height:1}
.socials{left:55px;top:1136px;display:flex;gap:3px}
.socials i{width:12px;height:12px;border:1px solid var(--footer-text);border-radius:50%}
.col{color:var(--footer-text)}
.col h4{font-size:7.5px;font-weight:700;text-transform:uppercase;margin-bottom:7px}
.col li{list-style:none;font-family:"Poppins",sans-serif;font-size:5px;line-height:14.5px;text-transform:uppercase}
.col-links{left:171px;top:1107px}
.col-contact{left:257px;top:1107px}
.col-news{left:388px;top:1107px;width:150px}
.col-news p{font-family:"Poppins",sans-serif;font-size:5px;line-height:8px;width:100px}
.subscribe{margin-top:6px;width:124px;height:17px;border:1px solid #bbb;display:flex;align-items:center;justify-content:space-between;padding:0 6px;font-family:"Poppins",sans-serif;font-size:4.5px}
.copyright{left:0;top:1185px;width:557px;height:15px;background:var(--footer-deep);border-top:1px solid #444;font-family:"Poppins",sans-serif;font-size:4px;color:#ccc;display:flex;align-items:center;justify-content:center}
</style>
</head>
<body>
<main class="page">

  <header>
    <div class="abs brand">coral ridge</div>
    <nav class="abs nav">
      <span>Home</span><span>About</span><span>Service</span><span>Contact</span>
      <span class="btn">Sign up</span>
    </nav>
  </header>

  <section class="hero-block">
    <div class="abs hero" role="img" aria-label="Photo of a site worker in a hard hat and high-visibility vest holding a clipboard near power lines"></div>
    <h1 class="abs hero-title">CORAL RIDGE</h1>
    <p class="abs hero-copy">At Coral Ridge Networks Ltd Safety is number one. Coral Ridge Ltd is committed to a strong safety policy, protecting its staff and the general public from accidents and harm. All Coral Ridge Employees are certified "Tower Competent Climber and Rescue".</p>
    <ul class="abs checks">
      <li><svg width="8" height="8" viewBox="0 0 10 10"><circle cx="5" cy="5" r="4.3" fill="none" stroke="#fff" stroke-width="1"/><path d="M3 5.2l1.4 1.4L7 3.8" fill="none" stroke="#fff" stroke-width="1"/></svg>COR Certified</li>
      <li><svg width="8" height="8" viewBox="0 0 10 10"><circle cx="5" cy="5" r="4.3" fill="none" stroke="#fff" stroke-width="1"/><path d="M3 5.2l1.4 1.4L7 3.8" fill="none" stroke="#fff" stroke-width="1"/></svg>BC Level 1 first aid</li>
      <li><svg width="8" height="8" viewBox="0 0 10 10"><circle cx="5" cy="5" r="4.3" fill="none" stroke="#fff" stroke-width="1"/><path d="M3 5.2l1.4 1.4L7 3.8" fill="none" stroke="#fff" stroke-width="1"/></svg>Transportation Endorsement first aid</li>
      <li><svg width="8" height="8" viewBox="0 0 10 10"><circle cx="5" cy="5" r="4.3" fill="none" stroke="#fff" stroke-width="1"/><path d="M3 5.2l1.4 1.4L7 3.8" fill="none" stroke="#fff" stroke-width="1"/></svg>Sprat Level 1</li>
      <li><svg width="8" height="8" viewBox="0 0 10 10"><circle cx="5" cy="5" r="4.3" fill="none" stroke="#fff" stroke-width="1"/><path d="M3 5.2l1.4 1.4L7 3.8" fill="none" stroke="#fff" stroke-width="1"/></svg>On site tailboard meeting with daily checklist sign off and picture documentation</li>
      <li><svg width="8" height="8" viewBox="0 0 10 10"><circle cx="5" cy="5" r="4.3" fill="none" stroke="#fff" stroke-width="1"/><path d="M3 5.2l1.4 1.4L7 3.8" fill="none" stroke="#fff" stroke-width="1"/></svg>Monthly in office safety meetings</li>
      <li><svg width="8" height="8" viewBox="0 0 10 10"><circle cx="5" cy="5" r="4.3" fill="none" stroke="#fff" stroke-width="1"/><path d="M3 5.2l1.4 1.4L7 3.8" fill="none" stroke="#fff" stroke-width="1"/></svg>Job site specific hazard assessment and reporting</li>
    </ul>
    <div class="abs hero-bar"></div>
  </section>

  <section class="about">
    <h2 class="abs h2 about-title">About us</h2>
    <div class="abs about-copy">
      <p>At Coral Ridge Ltd, we are dedicated to providing our customers with friendly professional service. We value your business. We have made it our mission to provide reliable products and services in our customer-driven approach.</p>
      <p>Our courteous, professional team is able to support a range of services to meet your requirements.</p>
      <p>To learn more about Coral Ridge Ltd, and the products and services we can offer, <strong>1-604-555-0182.</strong></p>
    </div>
    <span class="abs btn call-btn">Call us</span>
    <div class="abs deco deco-top"></div>
    <div class="abs deco deco-bottom"></div>
    <div class="abs about-photo" role="img" aria-label="Photo of a worker raising a hand toward a transmission tower at sunset"></div>
  </section>

  <section class="services">
    <h2 class="abs h2 service-title">Our service</h2>
    <article class="abs card" style="left:50px">
      <div class="card-photo" role="img" aria-label="Photo of rooftop telecom equipment under a blue sky" style="background:linear-gradient(180deg,#4f86cf 0%,#a9c6e6 55%,#8b8f92 100%)"></div>
      <h3>Rooftop sites</h3>
      <p>Structural upgrades on ballast mounts, shelter and ground grounding cable trays or conduits on the roof. Coral Ridge can build what you need where you need it.</p>
      <span class="more">Learn more <svg width="7" height="4" viewBox="0 0 7 4"><path d="M0 2h6M4.5 .5L6 2 4.5 3.5" fill="none" stroke="currentColor" stroke-width=".7"/></svg></span>
    </article>
    <article class="abs card is-active" style="left:207px">
      <div class="card-photo" role="img" aria-label="Photo of a cellular tower with antennas against the sky" style="background:linear-gradient(180deg,#2f4d78 0%,#6f8fb6 60%,#c9d3de 100%)"></div>
      <h3>Towers and monopoles</h3>
      <p>Coral Ridge can engineer, supply and install all your tower needs. New structures or existing, call us for pricing, we would be happy to help out.</p>
      <span class="more">Learn more <svg width="7" height="4" viewBox="0 0 7 4"><path d="M0 2h6M4.5 .5L6 2 4.5 3.5" fill="none" stroke="currentColor" stroke-width=".7"/></svg></span>
    </article>
    <article class="abs card" style="left:365px">
      <div class="card-photo" role="img" aria-label="Photo of a snowy summit with a slim tower under a blue sky" style="background:linear-gradient(180deg,#3e79c4 0%,#9fc0e3 55%,#eef3f8 100%)"></div>
      <h3>In building</h3>
      <p>Small office or large hotel, Coral Ridge has installed services into all size buildings. Fiber, CAT6, or coax, we have the abilities to install, test and get the job done.</p>
      <span class="more">Learn more <svg width="7" height="4" viewBox="0 0 7 4"><path d="M0 2h6M4.5 .5L6 2 4.5 3.5" fill="none" stroke="currentColor" stroke-width=".7"/></svg></span>
    </article>
  </section>

  <section class="contact-block">
    <h2 class="abs h2 contact-title">Contact us</h2>
    <div class="abs contact-panel"></div>
    <div class="abs map" role="img" aria-label="Street map showing the office location"></div>
    <div class="abs map-card">4175 Harbour Line<span>View Larger Map</span><i></i></div>
    <div class="abs field" style="top:823px;height:23px">Full name</div>
    <div class="abs field" style="top:855px;height:23px">E-mail</div>
    <div class="abs field" style="top:885px;height:23px">E-mail</div>
    <div class="abs field" style="top:915px;height:104px">Message</div>
    <span class="abs btn send-btn">Send</span>
  </section>

  <footer class="site-footer">
    <div class="abs footer"></div>
    <div class="abs foot-brand">coral ridge</div>
    <div class="abs socials"><i></i><i></i><i></i><i></i></div>
    <div class="abs col col-links">
      <h4>Quick link</h4>
      <ul><li>Home</li><li>About</li><li>Service</li><li>Contact</li></ul>
    </div>
    <div class="abs col col-contact">
      <h4>Contact</h4>
      <ul><li>1-604-555-0182</li><li>info@coralridgenet.ca</li><li>4175 Harbour Line, Fernwood, BC V3K 1R8</li></ul>
    </div>
    <div class="abs col col-news">
      <h4>Subscribe newsletter</h4>
      <p>Get project news and safety updates from our field crews each month.</p>
      <div class="subscribe"><span>Enter Your Email</span>
        <svg width="6" height="6" viewBox="0 0 6 6"><circle cx="2.5" cy="2.5" r="1.8" fill="none" stroke="#fff" stroke-width=".7"/><path d="M3.8 3.8L5.6 5.6" stroke="#fff" stroke-width=".7"/></svg>
      </div>
    </div>
    <div class="abs copyright">Copyright 2022 Coral Ridge Ltd</div>
  </footer>

</main>
</body>
</html>
```